Professional Business Card for Luxury Hotel & Resort Development Firm. Advisory firm

Project Overview: We are a specialized advisory firm focused on Hotel & Resort Development. Our clients are high-net-worth investors and major hospitality brands.

Design Requirements:

Style: Minimalist, sophisticated, and trustworthy. We want to avoid looking too "corporate" or "dry"—it should feel premium.

Key Elements: Please incorporate our logo [もしロゴがあれば] and emphasize a clean layout with plenty of white space.

Color Palette: We prefer Grey and White or Black and White to evoke a sense of luxury and stability.

Typography: Professional garamond, or sans-serif or elegant serif fonts

Goal: The card should feel substantial and high-end when handed to a client, reflecting our expertise in multi-million dollar developments.
Updates

I am currently on a business trip for field research and have limited access to my desktop. Additionally, I have just provided detailed technical feedback to a designer and am waiting for their refined proposals. To ensure the final logo meets the high standards of my new advisory firm, I would like to extend the deadline by 7 days. Thank you for your support.

Target Market(s)

High-net-worth investors, luxury hospitality brands, and real estate developers.

Contact Information for Business Card

Firm Name: Larkfield Counsel Partners, My Name: Kenji Morisawa, Title: Founder, Address 5-7-4 Kitakawabe Asahi Yokohama Japan 241-0815, email address: kmorisawa@larkfieldcp.com, Tel: +81 80-4821-3357. Front Site (Primary): Japanese translation of the back side, Please use a clean Japanese font (like Mincho) that complements the Garmond on the English side Back side: English. Note for Japanese text: since the frond side is the main fae, please ensure the layout is clean and professional. Please use a high-quality Mincho ( Serif-style) font for Japanese to mach the Garmond used on the English side. Text for Front side (Japanese) Larkfield Counsel Partners, 役職:代表、森沢健二、241-0815 横浜市旭区北川辺5-7-4. Name of the firm can stay in English.

Font styles to use
Other font styles liked:
• Font Preference: Please use Garamond for all text to maintain a consistent, elegant, and classic professional look.

Requirements
Must have
• Professional and clean layout, high-end feel.
Nice to have
• Minimalist design with subtle luxury accents.

```html
<!DOCTYPE html>
<html lang="en">
<head>
<meta charset="utf-8">
<title>Larkfield Counsel Partners – Business Card</title>
<link rel="stylesheet" href="https://fonts.googleapis.com/css2?family=Cormorant+Garamond:ital,wght@0,400;0,500;0,600;1,400&family=Noto+Sans+JP:wght@400&display=swap">
<style>
  :root {
    --backdrop: #737980;
    --card-light: #ffffff;
    --card-dark: #383838;
    --ink-dark: #555555;
    --ink-light: #f3f3f3;
    --rule-dark: #4a4a4a;
    --rule-light: #d8d8d8;
  }
  * { margin: 0; padding: 0; box-sizing: border-box; }
  html, body { width: 1200px; height: 929px; overflow: hidden; }
  body {
    position: relative;
    background: var(--backdrop);
    font-family: "Cormorant Garamond", Garamond, serif;
  }
  .card {
    position: absolute;
    width: 367px;
    height: 626px;
    text-align: center;
  }
  .card--front { left: 175px; top: 160px; background: var(--card-light); color: var(--ink-dark); }
  .card--back { left: 641px; top: 159px; background: var(--card-dark); color: var(--ink-light); }

  .line { position: absolute; left: 0; right: 0; white-space: nowrap; }

  .firm-name {
    top: 122px;
    font-size: 22px;
    line-height: 21px;
    font-weight: 500;
    letter-spacing: 0.3px;
  }
  .rule { position: absolute; left: 54px; right: 54px; height: 1px; }
  .card--front .rule { background: var(--rule-dark); }
  .card--back .rule { background: var(--rule-light); }

  .jp { font-family: "Noto Sans JP", sans-serif; }
  .front-title { top: 402px; font-size: 20px; line-height: 26px; }
  .front-name { top: 430px; font-size: 30px; line-height: 40px; letter-spacing: 1px; }
  .front-postal { top: 508px; font-size: 17px; line-height: 22px; }
  .front-address { top: 536px; font-size: 17px; line-height: 24px; }
  .front-address .num { font-family: "Cormorant Garamond", Garamond, serif; }

  .back-name { top: 308px; font-size: 21px; line-height: 28px; font-weight: 600; letter-spacing: 0.6px; }
  .back-title { top: 341px; font-size: 20px; line-height: 26px; font-style: italic; }
  .back-address { top: 405px; font-size: 17px; line-height: 23.5px; }
  .back-contact { top: 512px; font-size: 17px; line-height: 21px; }
</style>
</head>
<body>
  <section class="card card--front" lang="ja">
    <p class="line firm-name">Larkfield Counsel<br>Partners</p>
    <p class="line jp front-title">代表</p>
    <p class="line jp front-name">森沢健二</p>
    <div class="rule" style="top:487px"></div>
    <p class="line front-postal">241-0815</p>
    <p class="line jp front-address">横浜市旭区北川辺 <span class="num">5-7-4</span></p>
  </section>

  <section class="card card--back">
    <p class="line firm-name">Larkfield Counsel<br>Partners</p>
    <p class="line back-name">KENJI MORISAWA</p>
    <p class="line back-title">Founder</p>
    <div class="rule" style="top:386px"></div>
    <p class="line back-address">5-7-4 Kitakawabe,<br>Asahi,<br>Yokohama Japan 241-0815</p>
    <div class="rule" style="top:497px"></div>
    <p class="line back-contact">kmorisawa@larkfieldcp.com<br>+81 80-4821-3357</p>
  </section>
</body>
</html>
```